Mailer Ad for Private Gym

We need a clean and modern front and back mailer for our upscale, modern gym. Must follow project brief and be cohesive with our current brand. We have uploaded the layout sketch in the brief as well. Please refer to our website corevaultfitness.example for additional branding, logo, and gym info.

Target Market(s)

high-end upscale market

Industry/Entity Type

Gym

Font styles to use
Sans Serif

Colors
ec1f27
ffffff

Requirements
Must have
• *** EXACT LAYOUT OF FRONT AND BACK OF POST CARD ATTACHED TO BRIEF.
• Please include:
• FRONT:
• Icons attached from our website: Weight loss, Build Strength, etc
• THE OFFER: "20% Off 2 Weeks of Personal Training*
• *Please see see back for details"
• BOTTOM COPY: Adjacent to Harlow College on Pell Avenue
• BACK SIDE:
• Attached shot of Gym
• ITALICS: *To redeem this offer, email us at contact@corevaultfitness.example with the subject line "Around the Corner". Offer is good for 20% off 2 weeks of personal training. The minimum amount of sessions is 2 per week. Offer good until 11.30.16
• (final design will also need expiration dates of 1/31/17 2/28/17 and 3/31/17)
• ~ Phone, Address, website at the bottom:
• 482 Pell Avenue, Durham, NC
• contact@corevaultfitness.example
• corevaultfitness.example
• 919.555.0147
• ~ Leave the right left blank for the address
• MUST BE clean, so it is easy to read.
• Stick to white postcard with grey, black, bright red/orange like website and logo
Should not have
• Crowded, messy, design.

```html
<!DOCTYPE html>
<html lang="en">
<head>
<meta charset="utf-8">
<title>Corevault – Personal Training Mailer</title>
<link rel="stylesheet" href="https://fonts.googleapis.com/css2?family=Mulish:wght@700;800;900&family=Arimo:ital,wght@0,400;0,700;1,700&display=swap">
<style>
  :root {
    --red: #ee4123;
    --red-deep: #ec1f27;
    --ink: #58595b;
    --ink-dark: #4d4e50;
    --white: #ffffff;
    --paper: #f7f7f7;
    --paper-shade: #e9e9e9;
    --rule-light: #d6d6d6;
    --rule-dark: #9c9c9c;
  }
  * { box-sizing: border-box; margin: 0; padding: 0; }
  html, body {
    width: 1200px; height: 776px; overflow: hidden;
    background: var(--white);
    font-family: "Mulish", "Helvetica Neue", Arial, sans-serif;
  }
  .mailer {
    position: relative; width: 1200px; height: 776px;
    background: var(--white);
  }
  .panel {
    position: absolute; left: 18px; right: 18px;
  }
  .masthead {
    top: 18px; height: 222px;
    background: linear-gradient(180deg, var(--white) 0%, var(--paper) 60%, var(--paper-shade) 100%);
  }
  .divider {
    position: absolute; left: 18px; right: 18px; height: 12px;
    background: linear-gradient(90deg, var(--rule-light) 0%, var(--rule-dark) 10%, #c9c9c9 50%, var(--rule-dark) 90%, var(--rule-light) 100%);
    box-shadow: 0 3px 4px rgba(0,0,0,0.12);
  }
  .divider--top { top: 238px; }
  .divider--bottom { top: 538px; }
  .services { top: 250px; height: 288px; background: var(--white); }
  .footer-zone {
    top: 550px; height: 208px;
    background: linear-gradient(180deg, var(--paper-shade) 0%, var(--paper) 40%, var(--white) 100%);
  }

  /* Brand */
  .brand { position: absolute; left: 38px; top: 72px; }
  .brand__name {
    display: flex; align-items: center; gap: 10px;
    font-weight: 900; font-size: 60px; line-height: 1;
    color: var(--ink); letter-spacing: -1px;
  }
  .brand__mark { width: 22px; height: 22px; background: var(--red); }
  .brand__tagline {
    margin-top: 14px; font-weight: 800; font-size: 14.5px;
    letter-spacing: 4.4px; color: var(--ink);
  }

  /* Offer */
  .offer {
    position: absolute; left: 415px; top: 50px; width: 369px; height: 147px;
    background: var(--red); color: var(--white);
    font-family: "Arimo", Arial, sans-serif; text-align: center;
    padding-top: 20px;
  }
  .offer::after {
    content: ""; position: absolute; inset: 6px;
    border: 1px dotted rgba(255,255,255,0.45);
  }
  .offer__lead { font-weight: 700; font-size: 17px; letter-spacing: 0.2px; }
  .offer__deal { margin-top: 4px; font-weight: 700; line-height: 1; }
  .offer__get { font-size: 22px; vertical-align: 14px; }
  .offer__pct { font-size: 48px; }
  .offer__note { margin-top: 8px; font-size: 18px; }

  .award {
    position: absolute; left: 905px; top: 47px; width: 176px; height: 176px;
    border-radius: 50%; background: var(--red);
  }

  /* Services */
  .services__title {
    position: absolute; left: 0; right: 0; top: 300px; text-align: center;
    font-weight: 800; font-size: 53px; color: var(--ink); letter-spacing: 0.3px;
  }
  .service {
    position: absolute; top: 392px; width: 320px; text-align: center;
  }
  .service--weight { left: 73px; }
  .service--strength { left: 429px; }
  .service--flex { left: 781px; }
  .service__icon { height: 70px; display: block; margin: 0 auto; }
  .service__label {
    margin-top: 18px; font-weight: 800; font-size: 28px; color: var(--ink);
  }

  /* Footer */
  .banner {
    position: absolute; left: 18px; right: 18px; top: 601px; height: 66px;
    background: var(--ink);
    display: flex; align-items: center; justify-content: center;
    color: var(--white); font-weight: 800; font-size: 33px; letter-spacing: 5.6px;
  }
  .location {
    position: absolute; left: 0; right: 0; top: 705px; text-align: center;
    font-family: "Arimo", Arial, sans-serif; font-style: italic; font-weight: 700;
    font-size: 22px; color: var(--red-deep);
  }
</style>
</head>
<body>
<main class="mailer">
  <section class="panel masthead"></section>
  <section class="panel services"></section>
  <section class="panel footer-zone"></section>
  <div class="divider divider--top"></div>
  <div class="divider divider--bottom"></div>

  <div class="brand">
    <div class="brand__name"><span class="brand__mark"></span>COREVAULT</div>
    <div class="brand__tagline">PERSONAL TRAINING STUDIO</div>
  </div>

  <div class="offer">
    <p class="offer__lead">2 WEEKS OF PERSONAL TRAINING</p>
    <p class="offer__deal"><span class="offer__get">Get </span><span class="offer__pct">20% OFF</span></p>
    <p class="offer__note">(Please see see back for details)</p>
  </div>

  <div class="award" role="img" aria-label="Local award badge"></div>

  <h1 class="services__title">What can the Corevault do for you?</h1>

  <div class="service service--weight">
    <svg class="service__icon" viewBox="0 0 70 70" width="70" height="70" aria-hidden="true">
      <path d="M14 6 H56 Q64 6 64 16 L60 56 Q59 64 50 64 H20 Q11 64 10 56 L6 16 Q6 6 14 6 Z" fill="var(--red)"/>
      <circle cx="35" cy="27" r="14" fill="var(--white)"/>
      <circle cx="35" cy="27" r="10" fill="var(--red)"/>
      <line x1="35" y1="27" x2="40" y2="20" stroke="var(--white)" stroke-width="3" stroke-linecap="round"/>
      <rect x="33" y="40" width="4" height="14" fill="var(--white)"/>
      <rect x="25" y="52" width="20" height="4" fill="var(--white)"/>
    </svg>
    <p class="service__label">Weight Loss</p>
  </div>

  <div class="service service--strength">
    <svg class="service__icon" viewBox="0 0 76 70" width="76" height="70" aria-hidden="true">
      <rect x="2" y="29" width="6" height="12" fill="var(--red)"/>
      <rect x="10" y="17" width="7" height="36" rx="2" fill="var(--red)"/>
      <rect x="19" y="9" width="9" height="52" rx="2" fill="var(--red)"/>
      <rect x="28" y="31" width="20" height="8" fill="var(--red)"/>
      <rect x="48" y="9" width="9" height="52" rx="2" fill="var(--red)"/>
      <rect x="59" y="17" width="7" height="36" rx="2" fill="var(--red)"/>
      <rect x="68" y="29" width="6" height="12" fill="var(--red)"/>
    </svg>
    <p class="service__label">Build Strength</p>
  </div>

  <div class="service service--flex">
    <svg class="service__icon" viewBox="0 0 76 70" width="76" height="70" aria-hidden="true">
      <circle cx="12" cy="12" r="8" fill="var(--red)"/>
      <path d="M24 10 L56 34 L66 64" fill="none" stroke="var(--red)" stroke-width="9" stroke-linecap="round" stroke-linejoin="round"/>
      <path d="M50 30 L42 64" fill="none" stroke="var(--red)" stroke-width="9" stroke-linecap="round"/>
      <path d="M36 19 L20 34" fill="none" stroke="var(--red)" stroke-width="7" stroke-linecap="round"/>
    </svg>
    <p class="service__label">Increase Flexibility</p>
  </div>

  <div class="banner">PERSONAL TRAINING AT A PRIVATE GYM</div>
  <p class="location">Right across from the Harlow East Campus Wall on Pell Avenue</p>
</main>
</body>
</html>
```